Real Estate Company Looking for Business Card Designs for 3 Executives

Hello!
Thanks so much for considering our project! We are a real estate investment company located in Edmonton, Alberta called Marlbeck Group of Companies. We invest/develop both commercial and residential real estate and are looking to create 3 DOUBLE-SIDED business cards for 3 top executives in the company! (for some reason it won't let us select the double-sided option, but yes, the cards are double sided and would be happy to tip extra)

We have certain guidelines that we want our business cards to for sure follow - the back of the Business card has to be the Black Background Version of the Logo which has already been designed and linked as a file (first file). We want the entire back of the card to simply just be the black background logo. In terms of the front of the card, would like to see a smaller version of the white background logo (linked as the second file) in the top left hand corner - of course, feel free to get creative and we can make revisions together along the way! and Then after that, just text. We want the card to be sharp, clean, easy on the eyes and highly professional looking. We would like the card to include the Full name of the Company (Marlbeck Group of Companies), Name of the Person, Title, Phone, Email. If possible please provide the front part of the card for 3 people:

1) Marlbeck Group of Companies, Lena Okafor, Chief Financial Officer, 780-555-0162, lenaokafor@marlbeckgroup.example

2) Marlbeck Group of Companies, Tobias Okafor, Chief Executive Officer, 780-555-0148, tobiasokafor@marlbeckgroup.example

3) Marlbeck Group of Companies, Rui Dalton, Chief Operations Officer, 587-555-0193, ruidalton@marlbeckgroup.example

Thank you so much for considering our project & we look forward to seeing your designs!

```html
<!DOCTYPE html>
<html lang="en">
<head>
<meta charset="utf-8">
<title>Marlbeck Business Card</title>
<link href="https://fonts.googleapis.com/css2?family=Karla:wght@400;500&family=Poppins:wght@600&display=swap" rel="stylesheet">
<style>
  :root {
    --stage: #1c1c1d;
    --card-dark-1: #6e6e70;
    --card-dark-2: #2e2d2f;
    --card-dark-3: #161517;
    --card-light: #fbfbfa;
    --ink: #111111;
    --ink-soft: #2a2a2a;
    --mark-light: #d9d9da;
  }
  * { box-sizing: border-box; margin: 0; padding: 0; }
  html, body { width: 1200px; height: 874px; overflow: hidden; }
  body {
    background: var(--stage);
    font-family: "Karla", sans-serif;
    position: relative;
  }
  .card {
    position: absolute;
    left: 267px;
    width: 666px;
    height: 380px;
    border-radius: 26px;
    overflow: hidden;
  }
  .card-back { top: 32px; }
  .card-front { top: 462px; background: var(--card-light); color: var(--ink); }

  .back-art {
    position: absolute; inset: 0;
    background: linear-gradient(100deg, var(--card-dark-1) 0%, var(--card-dark-2) 38%, var(--card-dark-3) 100%);
  }
  .back-name {
    position: absolute; inset: 0;
    display: flex; align-items: center; justify-content: center;
    font-family: "Karla", sans-serif;
    font-weight: 500;
    font-size: 40px;
    letter-spacing: 14px;
    color: var(--mark-light);
  }

  .brand {
    position: absolute; right: 48px; top: 78px;
    display: flex; align-items: center; gap: 12px;
    font-weight: 500; font-size: 22px; letter-spacing: 8px;
    color: var(--ink);
  }
  .brand-square { width: 14px; height: 14px; background: var(--ink); }

  .person { position: absolute; left: 44px; top: 205px; }
  .person-name {
    font-family: "Poppins", sans-serif; font-weight: 600;
    font-size: 26px; letter-spacing: 1px; line-height: 1;
  }
  .person-title { font-size: 15px; color: var(--ink-soft); margin-top: 4px; }

  .rule {
    position: absolute; left: 40px; right: 40px; top: 262px;
    height: 1.5px; background: var(--ink);
  }
  .contacts { position: absolute; left: 44px; top: 276px; list-style: none; }
  .contacts li {
    display: flex; align-items: center; gap: 10px;
    font-size: 16px; line-height: 26px; color: var(--ink-soft);
  }
  .contacts svg { width: 12px; height: 12px; fill: var(--ink); }
  .website {
    position: absolute; right: 44px; top: 302px;
    font-size: 17px; font-weight: 500;
  }
</style>
</head>
<body>
  <section class="card card-back">
    <div class="back-art" role="img" aria-label="Black background version of the company logo with forest motif"></div>
    <div class="back-name">MARLBECK</div>
  </section>

  <section class="card card-front">
    <div class="brand"><span class="brand-square"></span>MARLBECK</div>

    <div class="person">
      <h1 class="person-name">LENA OKAFOR</h1>
      <p class="person-title">Chief Financial Officer</p>
    </div>

    <div class="rule"></div>

    <ul class="contacts">
      <li>
        <svg viewBox="0 0 24 24" aria-hidden="true"><path d="M6.6 10.8a15.1 15.1 0 0 0 6.6 6.6l2.2-2.2a1 1 0 0 1 1-.25 11.4 11.4 0 0 0 3.6.57 1 1 0 0 1 1 1V20a1 1 0 0 1-1 1A17 17 0 0 1 3 4a1 1 0 0 1 1-1h3.5a1 1 0 0 1 1 1c0 1.25.2 2.45.57 3.57a1 1 0 0 1-.25 1z"/></svg>
        780-555-0162
      </li>
      <li>
        <svg viewBox="0 0 24 24" aria-hidden="true"><path d="M2 5h20v14H2z M3.5 6.5 12 12.5l8.5-6z" fill-rule="evenodd"/></svg>
        lenaokafor@marlbeckgroup.example
      </li>
    </ul>

    <p class="website">MarlbeckGroup.example</p>
  </section>
</body>
</html>
```